New DermaLoom logo and packaging

We would like a new design for our new product DermaLoom, a high strength vitamin C serum which treats pigmentation. The packaging will reflect a high quality, clinical product with the logo "DermaLoom" on the front, with it's ingredients "Vitamin C, B3, B5, E and ferulic acid" the products are in two sizes 10ml and 30ml.

This is one of many products to come out in the DermaLoom range.

It would be for high end medical clinics selling premium brands, with a strong medical and clinical feel, professional and current or even futuristic in appearance.

Gold, blue, silver, White, cream are all colours that do this (without appearing cheap)

The product is not tested on animals, so would have
- "Not tested on animals".
- "12m" symbol for shelf life,
- "Made in USA"
- and ingredients list

See attached the product and existing box

Target Market(s)

Medical and aesthetic clinics

Font styles to use
Serif
Sans Serif

Colors
33a6d7
cee9f5
ffffff
fbed22
fee18a

Requirements
Must have
• High end premium brand
Nice to have
• like the idea of gold and silver lettering on cream background
Should not have
• Tacky, over complicated design

```html
<!DOCTYPE html>
<html lang="en">
<head>
<meta charset="utf-8">
<title>DermaLoom Serum Carton – Flat Layout</title>
<link rel="stylesheet" href="https://fonts.googleapis.com/css2?family=Montserrat:wght@300;400;500;600&display=swap">
<style>
  :root {
    --backdrop: #a9b3b3;
    --cream-light: #fbef9e;
    --cream: #f3df7c;
    --cream-deep: #e4cf62;
    --gold-dark: #8a6d08;
    --gold-mid: #c9a41a;
    --gold-light: #f3dc6a;
    --blue: #33a6d7;
    --blue-light: #47c3ea;
    --ice: #cee9f5;
    --silver: #c3cbcd;
    --white: #ffffff;
    --ink: #1c1a10;
  }
  * { margin: 0; padding: 0; box-sizing: border-box; }
  html, body { width: 1200px; height: 1050px; overflow: hidden; }
  body {
    background: radial-gradient(ellipse at 50% 40%, #b8c2c2 0%, var(--backdrop) 60%, #8f9898 100%);
    font-family: "Montserrat", sans-serif;
    color: var(--ink);
    position: relative;
  }
  .carton { position: absolute; left: 320px; top: 80px; width: 540px; height: 890px; }

  .panel { position: absolute; overflow: hidden; }

  .top-flap {
    left: 240px; top: 0; width: 300px; height: 240px;
    background: linear-gradient(135deg, var(--blue) 0%, var(--blue-light) 100%);
    display: flex; flex-direction: column; align-items: center; justify-content: center;
    color: var(--ice);
  }
  .top-flap .top-name { font-size: 38px; font-weight: 400; letter-spacing: 0.5px; }
  .top-flap .top-by { font-size: 15px; font-weight: 400; align-self: flex-end; margin-right: 44px; margin-top: -2px; }

  .side-panel {
    left: 0; top: 240px; width: 240px; height: 650px;
    background: linear-gradient(180deg, var(--cream) 0%, var(--cream-deep) 100%);
  }
  .front-panel {
    left: 240px; top: 240px; width: 300px; height: 650px;
    background: linear-gradient(160deg, var(--cream-deep) 0%, var(--cream-light) 35%, var(--cream) 60%, var(--cream-light) 100%);
  }

  .ingredients {
    position: absolute; top: 170px; left: 0; width: 100%;
    text-align: center; font-size: 18px; line-height: 1.3; font-weight: 400;
  }
  sub { font-size: 0.6em; }

  .claims { position: absolute; left: 40px; top: 460px; display: flex; align-items: flex-start; gap: 10px; }
  .shelf-life-icon { width: 30px; height: 38px; }
  .animal-claim { font-size: 14px; line-height: 1.25; padding-top: 12px; }

  .label-area {
    position: absolute; left: 38px; top: 520px; width: 162px; height: 60px;
    background: var(--silver); border: 3px solid var(--white); border-bottom: 0;
  }

  .base-band {
    position: absolute; left: 0; bottom: 0; width: 100%; height: 70px;
    background: linear-gradient(90deg, var(--blue) 0%, #3ab3de 100%);
    display: flex; align-items: center; justify-content: center;
    color: var(--ice); font-size: 16px; font-weight: 400;
  }
  .front-panel .base-band { font-size: 22px; letter-spacing: 0.3px; }

  .brand-plate {
    position: absolute; left: 0; top: 170px; width: 300px; height: 120px;
    background: linear-gradient(120deg, var(--gold-dark) 0%, var(--gold-mid) 35%, var(--gold-light) 50%, var(--gold-mid) 65%, var(--gold-dark) 100%);
    display: flex; flex-direction: column; justify-content: center; align-items: flex-start;
    padding: 0 20px;
    color: var(--cream-light);
  }
  .brand-name { font-size: 42px; font-weight: 500; line-height: 1; letter-spacing: -0.5px; white-space: nowrap; }
  .brand-by { font-size: 18px; font-weight: 500; align-self: flex-end; margin-top: 4px; }

  .front-actives {
    position: absolute; left: 0; bottom: 110px; width: 100%;
    text-align: center; font-size: 21px; line-height: 1.25; font-weight: 400;
  }
</style>
</head>
<body>
  <main class="carton">
    <section class="panel top-flap">
      <div class="top-name">DermaLoom</div>
      <div class="top-by">by Orvella</div>
    </section>

    <section class="panel side-panel">
      <p class="ingredients">Ingredients:<br>Vitamin C, B<sub>3</sub>, B<sub>5</sub>, E<br>and Ferulic Acid</p>
      <div class="claims">
        <svg class="shelf-life-icon" viewBox="0 0 30 38" aria-label="12 month shelf life">
          <ellipse cx="18" cy="6" rx="10" ry="4" fill="none" stroke="#1c1a10" stroke-width="2.5"/>
          <path d="M3 12 H27 V35 H3 Z" fill="#1c1a10"/>
          <text x="15" y="28" text-anchor="middle" font-family="Montserrat, sans-serif" font-size="9" fill="#f3df7c">12M</text>
        </svg>
        <p class="animal-claim">Not Tested<br>On Animals</p>
      </div>
      <div class="label-area"></div>
      <div class="base-band">Made in USA</div>
    </section>

    <section class="panel front-panel">
      <div class="brand-plate">
        <div class="brand-name">DermaLoom</div>
        <div class="brand-by">by Orvella</div>
      </div>
      <p class="front-actives">Vitamin C, B<sub>3</sub>, B<sub>5</sub>, E<br>and Ferulic Acid</p>
      <div class="base-band">℮ 30 ml | 1 fl. oz</div>
    </section>
  </main>
</body>
</html>
```